Civic Bastion Business Cards
Business Card for Civic Bastion
Project: Civic Bastion Business Cards
Civic Bastion Business Cards - Law
Creative Brief
Professional
Dorian Hale
Chairman/CEO
384 S. Wren Hollow Dr. Suite 212 Houston, TX 77031
dorian@civicbastion.example
www.civicbastion.example
I need another version for the following partner (all other information remains the same except the following): Russell T. Monday Chief Legal Officer email: russ@civicbastion.example
I am thinking a bigger version of the logo on the front to be used on the back of the card. Along with: To file a claim, please call toll free 1.888.555-0147

```html
<!DOCTYPE html>
<html lang="en">
<head>
<meta charset="utf-8">
<title>Civic Bastion Business Cards</title>
<link href="https://fonts.googleapis.com/css2?family=Montserrat:wght@400;600;700&family=Cinzel:wght@500&display=swap" rel="stylesheet">
<style>
  :root {
    --backdrop: #5a5b5d;
    --card-white: #ffffff;
    --card-dark: #2a2a2c;
    --bronze: #c58a4e;
    --bronze-light: #e2ab6c;
    --ink: #3a3a3a;
    --ink-soft: #555555;
    --claim-text: #d9d9d9;
  }
  * { margin: 0; padding: 0; box-sizing: border-box; }
  html, body { width: 1200px; height: 840px; overflow: hidden; }
  body {
    background: var(--backdrop);
    font-family: "Montserrat", Arial, sans-serif;
    position: relative;
  }
  .shared-defs { position: absolute; width: 0; height: 0; }
  .card {
    position: absolute;
    width: 500px;
    height: 288px;
    overflow: hidden;
    border-radius: 3px;
    box-shadow: 0 8px 22px rgba(0,0,0,.35);
  }
  .card-front { left: 60px; background: var(--card-white); }
  .card-front.dorian { top: 112px; }
  .card-front.russell { top: 440px; }
  .card-back { left: 640px; top: 276px; background: var(--card-dark); }
  .card-art { position: absolute; inset: 0; width: 100%; height: 100%; }

  .identity { position: absolute; right: 28px; top: 36px; width: 200px; }
  .person-name { color: var(--bronze); font-size: 17px; font-weight: 600; letter-spacing: 1.5px; text-transform: uppercase; white-space: nowrap; }
  .person-title { color: var(--ink); font-size: 11px; font-weight: 700; letter-spacing: 1px; text-transform: uppercase; margin-top: 3px; white-space: nowrap; }

  .address { position: absolute; right: 28px; top: 112px; width: 200px; color: var(--ink-soft); font-size: 9px; line-height: 1.55; }
  .contact-list { position: absolute; right: 28px; top: 160px; width: 200px; list-style: none; }
  .contact-list li { display: flex; align-items: center; justify-content: space-between; color: var(--ink-soft); font-size: 9px; height: 19px; white-space: nowrap; }
  .contact-icon { width: 10px; height: 10px; fill: var(--bronze); flex: none; }

  .brand { position: absolute; left: 44px; top: 118px; display: flex; align-items: center; gap: 14px; }
  .brand-circle { width: 76px; height: 76px; border-radius: 50%; border: 3px solid var(--bronze); flex: none; }
  .brand-name { font-family: "Cinzel", Georgia, serif; font-weight: 500; color: var(--bronze-light); font-size: 24px; letter-spacing: 1px; text-transform: uppercase; white-space: nowrap; }
  .claim-line { position: absolute; left: 134px; top: 176px; color: var(--claim-text); font-size: 9.5px; letter-spacing: .4px; white-space: nowrap; }
  .claim-line strong { color: var(--bronze-light); font-weight: 600; }
</style>
</head>
<body>

<svg class="shared-defs" aria-hidden="true">
  <defs>
    <linearGradient id="bronzeFill" x1="0" y1="0" x2="1" y2="1">
      <stop offset="0" stop-color="#9a6230"/>
      <stop offset="0.45" stop-color="#d49a5c"/>
      <stop offset="1" stop-color="#a8703a"/>
    </linearGradient>
    <linearGradient id="silverFill" x1="0" y1="0" x2="1" y2="0">
      <stop offset="0" stop-color="#8e9195"/>
      <stop offset="0.5" stop-color="#e6e7e9"/>
      <stop offset="1" stop-color="#a7aaae"/>
    </linearGradient>
    <linearGradient id="bronzeSweep" x1="0" y1="0" x2="1" y2="1">
      <stop offset="0" stop-color="#e7b476"/>
      <stop offset="1" stop-color="#8f5a2a"/>
    </linearGradient>
    <symbol id="frontSwoosh" viewBox="0 0 520 300" preserveAspectRatio="none">
      <path d="M0 0 H300 C230 40 150 150 0 250 Z" fill="url(#bronzeFill)"/>
      <path d="M300 0 C230 40 150 150 0 250 L0 272 C170 170 240 60 330 0 Z" fill="#3b3d40"/>
      <path d="M330 0 C240 60 170 170 0 272 L0 290 C200 190 270 70 360 0 Z" fill="url(#silverFill)"/>
    </symbol>
    <symbol id="iconPhone" viewBox="0 0 10 10"><path d="M2 0.5 L3.6 0.5 L4.2 2.8 L3 3.6 Q4 5.8 6.4 7 L7.2 5.8 L9.5 6.4 L9.5 8 Q9.5 9.5 8 9.5 Q0.5 9 0.5 2 Q0.5 0.5 2 0.5 Z"/></symbol>
    <symbol id="iconMail" viewBox="0 0 10 10"><rect x="0.5" y="2" width="9" height="6.5"/><path d="M0.8 2.3 L5 5.6 L9.2 2.3" fill="none" stroke="#fff" stroke-width="0.9"/></symbol>
    <symbol id="iconWeb" viewBox="0 0 10 10"><circle cx="5" cy="5" r="4.5"/><path d="M0.5 5 H9.5 M5 0.5 Q2.5 5 5 9.5 M5 0.5 Q7.5 5 5 9.5" fill="none" stroke="#fff" stroke-width="0.7"/></symbol>
    <symbol id="iconPin" viewBox="0 0 10 10"><path d="M5 0.5 Q8.5 0.5 8.5 4 Q8.5 6.5 5 9.5 Q1.5 6.5 1.5 4 Q1.5 0.5 5 0.5 Z"/><circle cx="5" cy="4" r="1.4" fill="#fff"/></symbol>
  </defs>
</svg>

<section class="card card-front dorian" aria-label="Business card front, Dorian Hale">
  <svg class="card-art" aria-hidden="true"><use href="#frontSwoosh" width="100%" height="100%"/></svg>
  <div class="identity">
    <p class="person-name">Dorian Hale</p>
    <p class="person-title">Chairman/CEO</p>
  </div>
  <p class="address">384 S. Wren Hollow Dr. Suite 212<br>Houston, TX 77031</p>
  <ul class="contact-list">
    <li>Toll free 1.888.555-0147 <svg class="contact-icon"><use href="#iconPhone"/></svg></li>
    <li>dorian@civicbastion.example <svg class="contact-icon"><use href="#iconMail"/></svg></li>
    <li>www.civicbastion.example <svg class="contact-icon"><use href="#iconWeb"/></svg></li>
    <li>Houston, Texas <svg class="contact-icon"><use href="#iconPin"/></svg></li>
  </ul>
</section>

<section class="card card-front russell" aria-label="Business card front, Russell T. Monday">
  <svg class="card-art" aria-hidden="true"><use href="#frontSwoosh" width="100%" height="100%"/></svg>
  <div class="identity">
    <p class="person-name">Russell T. Monday</p>
    <p class="person-title">Chief Legal Officer</p>
  </div>
  <p class="address">384 S. Wren Hollow Dr. Suite 212<br>Houston, TX 77031</p>
  <ul class="contact-list">
    <li>Toll free 1.888.555-0147 <svg class="contact-icon"><use href="#iconPhone"/></svg></li>
    <li>russ@civicbastion.example <svg class="contact-icon"><use href="#iconMail"/></svg></li>
    <li>www.civicbastion.example <svg class="contact-icon"><use href="#iconWeb"/></svg></li>
    <li>Houston, Texas <svg class="contact-icon"><use href="#iconPin"/></svg></li>
  </ul>
</section>

<section class="card card-back" aria-label="Business card back">
  <svg class="card-art" viewBox="0 0 520 300" preserveAspectRatio="none" aria-hidden="true">
    <path d="M360 0 C450 50 490 120 520 170 L520 150 C495 100 450 40 390 0 Z" fill="url(#bronzeSweep)"/>
    <path d="M395 0 C460 40 500 100 520 130 L520 112 C500 80 470 35 425 0 Z" fill="#b07a44"/>
    <path d="M430 0 C480 30 505 60 520 85 L520 70 C505 45 485 20 460 0 Z" fill="#4a3a2c"/>
  </svg>
  <div class="brand">
    <span class="brand-circle"></span>
    <span class="brand-name">Civic Bastion LLC</span>
  </div>
  <p class="claim-line">To file a claim, please call toll free <strong>1.888.555-0147</strong></p>
</section>

</body>
</html>
```